Legal Industry Crowdsourcing Website

BrieflyNest.com will be a new crowdsourcing website. The audiences are law students and legal professionals, and individual citizens, predominantly those working for or running small businesses. The objective is to enable them to get cheap or free legal advice and opinions.

Think of it like MakerPool.com but for lawyers. NB: BrieflyNest.com is NOT a law firm.

Do not include pictures of gavels (the wooden hammers). They are not used in the courts of England & Wales.
Updates

Target Market(s)

Legal industry, small business owners

Industry/Entity Type

Lawyer

Number of Pages Required

1 page

Requirements
Must have
• It must show the information presented in the Powerpoint file attached to the brief
• Must also show how the page appears on mobile devices.
Should not have
• Should not have:
• Pictures of gavels (the wooden hammers). They are not used in the courts of England & Wales.
• A vertical ever-scrolling design

```html
<!DOCTYPE html>
<html lang="en">
<head>
<meta charset="utf-8">
<title>BrieflyNest – Home</title>
<link rel="stylesheet" href="https://fonts.googleapis.com/css2?family=Cinzel:wght@400;700&family=Open+Sans:wght@400;600;700&display=swap">
<style>
:root{
  --gold:#b8892a;
  --gold-dark:#9c7220;
  --ink:#2b2b2b;
  --muted:#6a6a6a;
  --white:#ffffff;
  --dark:#1d1d1d;
  --darker:#121212;
  --red:#b3261e;
}
*{box-sizing:border-box;margin:0;padding:0}
html,body{width:1200px;height:2387px;overflow:hidden;background:var(--white)}
body{position:relative;font-family:"Open Sans",Arial,sans-serif;color:var(--ink)}
.abs{position:absolute}

/* header */
.site-header{position:absolute;left:0;top:0;width:1200px;height:166px;background:var(--white)}
.brand{position:absolute;left:99px;top:92px;font-family:"Cinzel",serif;font-size:28px;color:var(--gold);letter-spacing:.5px;display:flex;align-items:center;gap:10px}
.brand-dot{width:22px;height:22px;border-radius:50%;background:var(--gold)}
.btn-account,.btn-brief{position:absolute;top:41px;height:32px;font-size:11.5px;font-weight:700;color:var(--white);display:flex;align-items:center;justify-content:center;gap:6px;border-radius:2px;text-transform:uppercase}
.btn-account{left:824px;width:121px;background:var(--gold)}
.btn-brief{left:979px;width:121px;background:#2a2a2a}
.main-nav{position:absolute;top:103px;left:0;width:1200px;font-size:12px;font-weight:600;color:#333;text-transform:uppercase}
.main-nav span{position:absolute;white-space:nowrap}
.main-nav .active{color:var(--gold)}
.main-nav .active::after{content:"";position:absolute;left:-4px;right:-4px;top:21px;height:3px;background:var(--gold)}

/* hero */
.hero{position:absolute;left:0;top:166px;width:1200px;height:514px;overflow:hidden}
.hero-photo{position:absolute;inset:0;background:linear-gradient(90deg,#6a3b22 0%,#a9713f 25%,#3a2a22 45%,#2c2424 60%,#8a5a33 80%,#5a3320 100%)}
.hero-shade{position:absolute;inset:0;background:rgba(20,12,8,.35)}
.hero-brand{position:absolute;left:0;width:1200px;top:262px;text-align:center;font-family:"Cinzel",serif;font-size:22px;color:var(--white)}
.hero-title{position:absolute;left:0;width:1200px;top:310px;text-align:center;font-family:"Cinzel",serif;font-weight:700;font-size:24.5px;line-height:34px;color:var(--white);letter-spacing:.4px}
.hero-cta,.hero-ghost{position:absolute;top:402px;height:43px;font-size:12.5px;font-weight:700;text-transform:uppercase;display:flex;align-items:center;justify-content:center}
.hero-cta{left:398px;width:189px;background:var(--gold);color:var(--white)}
.hero-ghost{left:613px;width:189px;border:2px solid var(--gold);color:#e2b85a}
.hero-arrow{position:absolute;top:244px}

/* issues */
.section-title{position:absolute;left:0;width:1200px;text-align:center;font-family:"Cinzel",serif;font-weight:700;font-size:27px;color:var(--gold)}
.intro{position:absolute;left:200px;width:800px;top:763px;text-align:center;font-size:11.5px;line-height:24px;color:var(--muted)}
.issue{position:absolute;width:250px;text-align:center}
.issue-icon{width:102px;height:102px;margin:0 auto;border-radius:50%;background:var(--gold);border:4px solid var(--white);box-shadow:0 0 0 2px var(--gold);display:flex;align-items:center;justify-content:center}
.issue-name{margin-top:19px;font-size:13px;font-weight:600;text-transform:uppercase;line-height:19px;color:#222;height:38px}
.issue-text{font-size:11px;line-height:18px;color:#666;width:190px;margin:0 auto}

/* advisors */
.advisors{position:absolute;left:0;top:1324px;width:1200px;height:439px;background:linear-gradient(90deg,#1a1410,#2c2018 40%,#1e1814 70%,#2a1d14)}
.advisor-card{position:absolute;top:51px;width:219px;height:353px;background:var(--white);padding:4px}
.advisor-photo{width:211px;height:148px}
.advisor-info{padding:8px 6px 0 6px;font-size:11.5px;line-height:22px;color:#444}
.advisor-info b{color:var(--gold);font-weight:700;text-transform:uppercase;font-size:11px}
.advisor-info .stars{color:var(--gold);letter-spacing:1px}
.advisor-ask{display:block;text-align:center;margin-top:2px;font-family:"Cinzel",serif;font-weight:700;font-size:14px;color:var(--red);text-decoration:underline}

/* news */
.news-item{position:absolute;top:1883px;width:330px;height:90px}
.news-date{position:absolute;left:0;top:0;width:79px;height:86px;background:var(--gold);color:var(--white);text-align:center;box-shadow:2px 3px 4px rgba(0,0,0,.25)}
.news-date .day{display:block;font-size:21px;margin-top:10px}
.news-date .month{display:block;font-size:12px;margin-top:3px}
.news-date .year{display:block;font-size:12px;margin-top:3px}
.news-body{position:absolute;left:101px;top:0;width:230px}
.news-title{font-family:"Cinzel",serif;font-weight:700;font-size:14px;color:var(--gold)}
.news-text{font-size:11px;line-height:17px;color:#555;margin-top:4px}
.news-meta{font-size:10.5px;color:#1e3c72;margin-top:6px;display:flex;align-items:center;gap:5px}

/* footer */
.site-footer{position:absolute;left:0;top:2029px;width:1200px;height:302px;background:var(--dark)}
.footer-col{position:absolute;top:37px}
.footer-col h3{font-family:"Cinzel",serif;font-weight:700;font-size:18px;color:var(--white);margin-bottom:16px;letter-spacing:.5px}
.footer-col ul{list-style:none}
.footer-col li{font-size:12px;color:#d8d8d8;line-height:17px;margin-bottom:12px;position:relative;padding-left:24px}
.footer-col li::before{content:"";position:absolute;left:0;top:5px;border-left:5px solid #ddd;border-top:4px solid transparent;border-bottom:4px solid transparent}
.footer-col .social li::before{display:none}
.social .mark{position:absolute;left:0;top:4px;width:9px;height:9px;border-radius:50%;background:#ddd}
.footer-col .link{color:var(--gold);text-decoration:underline}
.footer-brand{position:absolute;left:952px;top:232px;font-family:"Cinzel",serif;font-size:16px;color:#d0d0d0}
.footer-bar{position:absolute;left:0;top:2331px;width:1200px;height:56px;background:var(--darker);font-size:11.5px;color:#cfcfcf}
.footer-bar span{position:absolute;left:99px;top:20px}
</style>
</head>
<body>

<header class="site-header">
  <div class="brand"><span class="brand-dot"></span>BrieflyNest</div>
  <div class="btn-account">
    <svg width="11" height="11" viewBox="0 0 12 12"><circle cx="6" cy="4" r="2.6" fill="#fff"/><path d="M1 12a5 5 0 0 1 10 0z" fill="#fff"/></svg>My Account</div>
  <div class="btn-brief">
    <svg width="13" height="11" viewBox="0 0 14 12"><rect x="1" y="3" width="12" height="8" fill="none" stroke="#fff" stroke-width="1.5"/><path d="M1 3l6 4 6-4" fill="none" stroke="#fff" stroke-width="1.5"/></svg>Post a Brief</div>
  <nav class="main-nav">
    <span class="active" style="left:500px">Home</span>
    <span style="left:582px">Sectors</span>
    <span style="left:680px">Legal Advisors</span>
    <span style="left:824px">Browse Briefs</span>
    <span style="left:963px">How it Works</span>
    <span style="left:1088px"><svg width="12" height="12" viewBox="0 0 12 12"><circle cx="5" cy="5" r="3.6" fill="none" stroke="#b8892a" stroke-width="1.8"/><path d="M7.6 7.6L11 11" stroke="#b8892a" stroke-width="1.8"/></svg></span>
  </nav>
</header>

<section class="hero">
  <div class="hero-photo" role="img" aria-label="Two smiling barristers in black robes standing in a law library lined with leather-bound books"></div>
  <div class="hero-shade"></div>
  <svg class="hero-arrow" style="left:24px" width="14" height="40" viewBox="0 0 14 40"><path d="M12 2L2 20l10 18" fill="none" stroke="#fff" stroke-width="1.5" opacity=".7"/></svg>
  <svg class="hero-arrow" style="left:1162px" width="14" height="40" viewBox="0 0 14 40"><path d="M2 2l10 18L2 38" fill="none" stroke="#fff" stroke-width="1.5" opacity=".7"/></svg>
  <div class="hero-brand">BrieflyNest</div>
  <h1 class="hero-title">GET NUMEROUS LEGAL OPINIONS ON YOUR CASE,<br>AND SELECT YOUR MOST PREFERRED LEGAL ADVISOR</h1>
  <div class="hero-cta">Get Started Now</div>
  <div class="hero-ghost">See How it Works?</div>
</section>

<h2 class="section-title" style="top:720px">WHAT DOES YOUR ISSUE RELATE TO?</h2>
<p class="intro">Lorem ipsum dolor sit amet, consectetur adipiscing elit, sed do eiusmod tempor incididunt ut labore et dolore magna aliqua. Ut enim ad minim veniam, quis nostrud exercitation ullamco laboris nisi ut aliquip ex ea commodo consequat. Duis aute irure dolor in reprehenderit in voluptate velit esse cillum dolore eu fugiat nulla pariatur. Excepteur sint occaecat cupidatat non proident</p>

<div class="issue" style="left:66px;top:864px">
  <div class="issue-icon"><svg width="46" height="40" viewBox="0 0 46 40"><rect x="16" y="6" width="20" height="13" rx="2" fill="#fff" transform="rotate(-20 26 12)"/><path d="M2 30h10l8 4h12l10-8-3-2-9 5H22" fill="none" stroke="#fff" stroke-width="3"/></svg></div>
  <div class="issue-name">Purchase and Supply</div>
  <p class="issue-text">Lorem ipsum dolor sit amet, scing ut labore et dolore magna ...</p>
</div>
<div class="issue" style="left:344px;top:864px">
  <div class="issue-icon"><svg width="40" height="40" viewBox="0 0 40 40"><rect x="3" y="3" width="22" height="22" fill="none" stroke="#fff" stroke-width="3"/><rect x="15" y="15" width="22" height="22" fill="none" stroke="#fff" stroke-width="3"/><path d="M10 10l14 14" stroke="#fff" stroke-width="3"/></svg></div>
  <div class="issue-name">Someone Copying My Work</div>
  <p class="issue-text">Lorem ipsum dolor sit amet, scing ut labore et dolore magna ...</p>
</div>
<div class="issue" style="left:618px;top:864px">
  <div class="issue-icon"><svg width="38" height="42" viewBox="0 0 38 42"><rect x="3" y="3" width="24" height="34" fill="none" stroke="#fff" stroke-width="3"/><path d="M8 12h14M8 18h14M8 24h8" stroke="#fff" stroke-width="2.5"/><path d="M20 34l14-16 3 3-14 16h-3z" fill="#fff"/></svg></div>
  <div class="issue-name">Agreements or Contracts</div>
  <p class="issue-text">Lorem ipsum dolor sit amet, scing ut labore et dolore magna ...</p>
</div>
<div class="issue" style="left:881px;top:864px">
  <div class="issue-icon"><svg width="46" height="38" viewBox="0 0 46 38"><circle cx="23" cy="8" r="6" fill="#fff"/><path d="M13 22a10 8 0 0 1 20 0z" fill="#fff"/><circle cx="10" cy="20" r="5" fill="#fff"/><path d="M2 34a8 7 0 0 1 16 0z" fill="#fff"/><circle cx="36" cy="20" r="5" fill="#fff"/><path d="M28 34a8 7 0 0 1 16 0z" fill="#fff"/></svg></div>
  <div class="issue-name">The Relationship Between Employer and Employee(s)</div>
  <p class="issue-text">Lorem ipsum dolor sit amet, scing ut labore et dolore magna ...</p>
</div>

<div class="issue" style="left:66px;top:1081px">
  <div class="issue-icon"><svg width="32" height="40" viewBox="0 0 32 40"><circle cx="16" cy="10" r="8" fill="#fff"/><path d="M2 40a14 16 0 0 1 28 0z" fill="#fff"/><rect x="18" y="26" width="8" height="8" fill="#b8892a"/></svg></div>
  <div class="issue-name">Injury to Person, Property or Reputation</div>
  <p class="issue-text">Lorem ipsum dolor sit amet, scing ut labore et dolore magna ...</p>
</div>
<div class="issue" style="left:344px;top:1081px">
  <div class="issue-icon"><svg width="44" height="42" viewBox="0 0 44 42"><circle cx="16" cy="9" r="6" fill="#fff"/><path d="M6 28a10 12 0 0 1 20 0z" fill="#fff"/><rect x="4" y="30" width="30" height="4" fill="#fff"/><path d="M28 24l12-16" stroke="#fff" stroke-width="3"/></svg></div>
  <div class="issue-name">The Duties of Government Agency or Department</div>
  <p class="issue-text">Lorem ipsum dolor sit amet, scing ut labore et dolore magna ...</p>
</div>
<div class="issue" style="left:618px;top:1081px">
  <div class="issue-icon"><svg width="44" height="38" viewBox="0 0 44 38"><path d="M22 3L3 19h5v16h28V19h5z" fill="none" stroke="#fff" stroke-width="3.5" stroke-linejoin="round"/><rect x="18" y="23" width="8" height="12" fill="#fff"/></svg></div>
  <div class="issue-name">Problems with Property</div>
  <p class="issue-text">Lorem ipsum dolor sit amet, scing ut labore et dolore magna ...</p>
</div>
<div class="issue" style="left:881px;top:1081px">
  <div class="issue-icon"><svg width="40" height="44" viewBox="0 0 40 44"><rect x="18" y="2" width="10" height="16" rx="3" fill="#fff"/><circle cx="10" cy="28" r="4" fill="#fff"/><circle cx="22" cy="28" r="4" fill="#fff"/><circle cx="33" cy="28" r="4" fill="#fff"/><path d="M4 42a6 7 0 0 1 12 0zM16 42a6 7 0 0 1 12 0zM27 42a6 7 0 0 1 12 0z" fill="#fff"/></svg></div>
  <div class="issue-name">The Content of a Will, the Operation of Trusts,</div>
  <p class="issue-text">Lorem ipsum dolor sit amet, scing ut labore et dolore magna ...</p>
</div>

<section class="advisors" role="img" aria-label="Dimmed law library background">
  <div class="advisor-card" style="left:99px">
    <div class="advisor-photo" role="img" aria-label="Portrait of a barrister in a court wig" style="background:linear-gradient(160deg,#c9a35a,#7a5a2e)"></div>
    <div class="advisor-info">
      <div><b>Advisor:</b> Rowan Aldous</div>
      <div><b>Occupation:</b> Barrister</div>
      <div><b>BrieflyNest Level:</b></div>
      <div style="margin-top:-5px">Barrister 1 year call</div>
      <div><b>Sector:</b> Commercial</div>
      <div><b>Briefs Answered:</b> 58</div>
      <div><b>Rating:</b> <span class="stars">★★★★★</span></div>
      <span class="advisor-ask">ASK ME FOR ADVICE</span>
    </div>
  </div>
  <div class="advisor-card" style="left:363px">
    <div class="advisor-photo" role="img" aria-label="Photo of a student working at a desk with a computer" style="background:linear-gradient(160deg,#9aa3a8,#c9c3bc)"></div>
    <div class="advisor-info">
      <div><b>Advisor:</b> Tessa Marlow</div>
      <div><b>Occupation:</b> Student</div>
      <div><b>BrieflyNest Level:</b></div>
      <div style="margin-top:-5px">Student</div>
      <div><b>Sector:</b> All</div>
      <div><b>Briefs Answered:</b> 2</div>
      <div><b>Rating:</b> <span class="stars">★★★★★</span></div>
      <span class="advisor-ask">ASK ME FOR ADVICE</span>
    </div>
  </div>
  <div class="advisor-card" style="left:624px">
    <div class="advisor-photo" role="img" aria-label="Black and white portrait of a solicitor in a suit" style="background:linear-gradient(160deg,#8c8c8c,#3a3a3a)"></div>
    <div class="advisor-info">
      <div><b>Advisor:</b> Owen Pritchard</div>
      <div><b>Occupation:</b> Solicitor</div>
      <div><b>BrieflyNest Level:</b></div>
      <div style="margin-top:-5px">Solicitor qualified for 6 years</div>
      <div><b>Sector:</b> Tort / Delict</div>
      <div><b>Briefs Answered:</b> 12</div>
      <div><b>Rating:</b> <span class="stars">★★★★★</span></div>
      <span class="advisor-ask">ASK ME FOR ADVICE</span>
    </div>
  </div>
  <div class="advisor-card" style="left:882px">
    <div class="advisor-photo" role="img" aria-label="Black and white portrait of a solicitor" style="background:linear-gradient(160deg,#d8d8d8,#555)"></div>
    <div class="advisor-info">
      <div><b>Advisor:</b> Nira Kessel</div>
      <div><b>Occupation:</b> Solicitor</div>
      <div><b>BrieflyNest Level:</b></div>
      <div style="margin-top:-5px">Solicitor qualified for 1 year</div>
      <div><b>Sector:</b> Commercial, Property, Tax</div>
      <div><b>Briefs Answered:</b> 5</div>
      <div><b>Rating:</b> <span class="stars">★★★★★</span></div>
      <span class="advisor-ask">ASK ME FOR ADVICE</span>
    </div>
  </div>
</section>

<h2 class="section-title" style="top:1808px">LATEST NEWS</h2>

<article class="news-item" style="left:99px">
  <div class="news-date"><span class="day">08</span><span class="month">December</span><span class="year">2015</span></div>
  <div class="news-body">
    <h3 class="news-title">FINIBUS BONORUM ET</h3>
    <p class="news-text">Lorem ipsum dolor sit amet, consectetur adipiscing elit, sed do eiusmod tempor</p>
    <div class="news-meta"><svg width="14" height="11" viewBox="0 0 14 11"><path d="M1 1h9v6H5l-3 3V7H1z" fill="#1e3c72"/><path d="M11 3h2v6h-1v2l-2-2H6" fill="none" stroke="#1e3c72"/></svg>34 comments</div>
  </div>
</article>
<article class="news-item" style="left:442px">
  <div class="news-date"><span class="day">08</span><span class="month">December</span><span class="year">2015</span></div>
  <div class="news-body">
    <h3 class="news-title">FINIBUS BONORUM ET</h3>
    <p class="news-text">Lorem ipsum dolor sit amet, consectetur adipiscing elit, sed do eiusmod tempor</p>
    <div class="news-meta"><svg width="14" height="11" viewBox="0 0 14 11"><path d="M1 1h9v6H5l-3 3V7H1z" fill="#1e3c72"/><path d="M11 3h2v6h-1v2l-2-2H6" fill="none" stroke="#1e3c72"/></svg>34 comments</div>
  </div>
</article>
<article class="news-item" style="left:778px">
  <div class="news-date"><span class="day">08</span><span class="month">December</span><span class="year">2015</span></div>
  <div class="news-body">
    <h3 class="news-title">FINIBUS BONORUM ET</h3>
    <p class="news-text">Lorem ipsum dolor sit amet, consectetur adipiscing elit, sed do eiusmod tempor</p>
    <div class="news-meta"><svg width="14" height="11" viewBox="0 0 14 11"><path d="M1 1h9v6H5l-3 3V7H1z" fill="#1e3c72"/><path d="M11 3h2v6h-1v2l-2-2H6" fill="none" stroke="#1e3c72"/></svg>34 comments</div>
  </div>
</article>

<footer class="site-footer">
  <div class="footer-col" style="left:99px">
    <h3>I NEED A?</h3>
    <ul>
      <li>Commercial Law Advisor</li>
      <li>Consumer Affairs Law Advisor</li>
      <li>Contract Law Advisor</li>
      <li>Intellectual Property Law Advisor</li>
      <li>Land / Property Law Advisor</li>
      <li>Equity, Wills &amp; Trusts Law Advisor</li>
    </ul>
  </div>
  <div class="footer-col" style="left:436px">
    <h3>ABOUT US</h3>
    <ul>
      <li>About us</li>
      <li>How it works</li>
      <li>Contact Us</li>
      <li>Affiliate Programme?</li>
      <li>Media</li>
      <li>Help / FAQ</li>
      <li>Social Media</li>
    </ul>
  </div>
  <div class="footer-col" style="left:697px">
    <h3>JURISDICTION</h3>
    <ul>
      <li>England &amp; Wales</li>
      <li>United States</li>
      <li>Scotland</li>
      <li>Australia</li>
      <li>Ireland</li>
      <li style="width:150px;line-height:14px">A Judicial Committee of the Privy Council Jurisdiction</li>
    </ul>
  </div>
  <div class="footer-col" style="left:958px">
    <h3>FOLLOW OUR?</h3>
    <ul class="social">
      <li><span class="mark"></span><span class="link">Newsletter</span></li>
      <li><span class="mark"></span>Chirpline</li>
      <li><span class="mark"></span>Friendwall</li>
      <li><span class="mark"></span>Workbond</li>
    </ul>
  </div>
  <div class="footer-brand">BrieflyNest</div>
</footer>
<div class="footer-bar"><span>© 2015 brieflynest.com All rights reserved</span></div>

</body>
</html>
```